New look and feel for investment website

Hi

Our website needs a crisp and professional look and feel applying to it. Here’s the address: http://www.brightplinth.co.uk. Since posting the brief yesterday (Tuesday, 16 August), we've reduced the amount of content on the home page, which should make life a little easier for you. We will come back later today, with some points of reference in terms of sites we like the look of. (See below)

17 August, 1.20pm GMT. OK, comments generally on the designs submitted so far. Please keep in mind that images of graphs, piles of coins, paper money and pretty females are not what is required. Better to think in terms of abstract imagery instead. Ratios? Circles? Relationships? Patterns? Not money,sex,graphs etc. Hope that helps.

For guidance on look and feel, please refer to these sites, which we like:

http://www.morvelle.co.uk/
http://www.qz.com/
https://www.harrowfieldtamsin.com
https://www.pirelconcerns.com
https://www.kvantule.com
Updates

Here's the Tall Beacons logo created in AI CS5.

Our market is professional financial advisers and relatively sophisticated private investors. The look and feel therefore should be slick and sophisticated - not 'lively' and lightweight, more like a banking site. Please read the brief again where we've added a list of websites that we really like the look of to get a better feel for what we're looking for. Thanks once again, we appreciate the work you're putting in.

It's essential that all the elements that are on the current home page be included on all new designs. 

We use a device in our e-mails which you may wish to incorporate in your design.

Target Market(s)

Professional financial advisers. People who know about investment and money.

Industry/Entity Type

Investment

Requirements
Should not have
• Graphs or people.

```html
<!DOCTYPE html>
<html lang="en">
<head>
<meta charset="utf-8">
<title>Tall Beacons</title>
<link rel="stylesheet" href="https://fonts.googleapis.com/css2?family=Arimo:ital,wght@0,400;0,700;1,700&display=swap">
<style>
  :root {
    --page-blue: #173a57;
    --topbar: #8c8c8c;
    --topbar-text: #f4f4f4;
    --hero-deep: #0e1c29;
    --hero-mid: #17344a;
    --accent-red: #c4313a;
    --accent-red-dark: #9b1f26;
    --headline-ink: #fbf1e6;
    --cream: #f4e9b6;
    --sidebar: #d5ca96;
    --ink: #111111;
    --muted: #8a8a8a;
    --nav-active: #a3191b;
    --divider: #ffffff;
    --stat-ink: #fbe9e9;
  }
  * { box-sizing: border-box; margin: 0; padding: 0; }
  html, body { width: 1200px; height: 900px; overflow: hidden; }
  body {
    background: var(--page-blue);
    font-family: "Arimo", Arial, sans-serif;
    color: var(--ink);
    position: relative;
  }
  .topbar {
    position: absolute; left: 0; top: 0; width: 1200px; height: 46px;
    background: var(--topbar);
    border-bottom: 1px solid #6f7a82;
  }
  .brand {
    position: absolute; left: 113px; top: 7px;
    font-size: 26px; font-weight: 700; color: #e2e2e2; letter-spacing: -0.5px;
    display: flex; align-items: center; gap: 4px;
  }
  .brand-dot { width: 5px; height: 5px; background: #e2e2e2; border-radius: 50%; margin-top: 6px; }
  .account-links {
    position: absolute; right: 133px; top: 14px;
    font-size: 14px; color: var(--topbar-text);
  }
  .hero {
    position: absolute; left: 130px; top: 46px; width: 940px; height: 405px;
    background: radial-gradient(ellipse at 70% 40%, var(--hero-mid), var(--hero-deep) 70%);
    border-bottom: 2px solid #d98a8a;
    overflow: hidden;
  }
  .headline {
    position: absolute; height: 56px;
    background: linear-gradient(var(--accent-red), var(--accent-red-dark));
    color: var(--headline-ink);
    font-size: 45px; line-height: 56px; padding: 0 4px;
    text-shadow: 0 1px 2px rgba(0,0,0,0.45);
    white-space: nowrap;
  }
  .headline-one { left: 93px; top: 89px; width: 457px; }
  .headline-two { left: 217px; top: 145px; width: 537px; padding-left: 7px; }
  .content {
    position: absolute; left: 130px; top: 451px; width: 720px; height: 449px;
    background: var(--cream);
    padding: 58px 100px 0 60px;
  }
  .intro-title {
    font-size: 22px; font-style: italic; font-weight: 700;
    color: var(--nav-active); margin: 0 0 22px 37px;
  }
  .content p { font-size: 14px; line-height: 17px; hyphens: auto; -webkit-hyphens: auto; }
  .content .lead { font-size: 18px; line-height: 22px; font-weight: 700; margin: 19px 0 16px; hyphens: none; }
  .content h3 { font-size: 14px; line-height: 17px; font-weight: 700; }
  .section { margin-bottom: 17px; }
  .sidebar {
    position: absolute; left: 850px; top: 451px; width: 220px; height: 449px;
    background: var(--sidebar);
  }
  .sidebar h2 {
    text-align: center; color: var(--muted); font-size: 18px; font-weight: 700;
  }
  .nav-title { margin-top: 29px; margin-bottom: 8px; }
  .nav-list { list-style: none; }
  .nav-list li {
    font-size: 13px; line-height: 15px; padding: 4px 0 3px 10px;
    border-bottom: 1px dashed var(--divider);
  }
  .nav-list li:last-child { border-bottom: none; }
  .nav-list .current { color: var(--nav-active); font-weight: 700; }
  .indent { padding-left: 21px; }
  .stats-title { margin: 18px 0 12px; }
  .stat {
    margin: 0 10px 19px 10px; height: 34px;
    background: linear-gradient(var(--accent-red), var(--accent-red-dark));
    box-shadow: 0 3px 4px rgba(0,0,0,0.35);
    color: var(--stat-ink); font-size: 13px; line-height: 15px;
    text-align: center; padding-top: 2px;
  }
</style>
</head>
<body>
  <header class="topbar">
    <div class="brand"><span>TallBeacons</span><span class="brand-dot"></span></div>
    <div class="account-links">Login | Register for Free</div>
  </header>

  <section class="hero" role="img" aria-label="Abstract dark blue backdrop for the headline">
    <div class="headline headline-one">Lorem ipsum dolor sit</div>
    <div class="headline headline-two">ut labore et dolore magna</div>
  </section>

  <main class="content">
    <h1 class="intro-title">Something different...</h1>
    <p>You may well be thinking that Tall Beacons is just another one of those banal share recommendation sites sprinkled with the usual idiotic and patronising platitudes, gross exaggerations, silly get-rich-quick promises and all the other stuff and nonsense you associate with the black art of share-tipping...</p>
    <p class="lead">Well, we have a pleasant surprise for you: you couldn't be further from the truth.</p>
    <div class="section">
      <h3>No! No! No!</h3>
      <p>There's no newsletter to read, books to study, dvds to watch or traders' secrets to be revealed. No never-ending stream of recommendations. No webcasts. No effort or time to invest. No training. No research. No tedious market commentaries. And no financial discomfort for you whatsoever. (At least for the first six months that is!)</p>
    </div>
    <div class="section">
      <h3>Undervalued and overlooked</h3>
      <p>Our program finds stocks that appear to be undervalued - i.e., where the price of a company's share does not reflect the real worth of the business. We confine our search to 1,000 of the USA's biggest companies; successful, robust, large cap businesses, which for one reason or another are either unpopular with investors or overlooked by them</p>
    </div>
  </main>

  <aside class="sidebar">
    <h2 class="nav-title">Navigation</h2>
    <ul class="nav-list">
      <li class="current">Home</li>
      <li>Two Minute Guide</li>
      <li>Current &amp; year to date performance</li>
      <li>Watch list</li>
      <li>Other key numbers</li>
      <li>Back tested results</li>
      <li>History of all trades</li>
      <li>FAQs</li>
      <li>About our analyses</li>
      <li>About value investing</li>
      <li>The Calder 1000<br><span class="indent">and the Norwick 500 index</span></li>
    </ul>
    <h2 class="stats-title">Stats</h2>
    <div class="stat">Average, annualised compound<br>return over to : 23.57 %</div>
    <div class="stat">So far this year, the portfolio's</div>
  </aside>
</body>
</html>
```